Flyer-Design für Food Truck Party Veranstaltung gesucht
Zielgruppe
Wir haben einen Food Truck und werden zum zweiten Mal in diesem Jahr für 7 Wochen ein Pop-Up Restaurant eröffnen!(Flyer für das erste Pop-Up Restaurant ist als Beispiel beigefügt, nur um zu verdeutlichen was wir machen, soll nicht so übernommen werden! Denn hier wird eher eine Party, als ein Restaurant suggeriert)
Zielgruppe sind Personen, die zwischen 30-70 Jahren sind, gerne Geld für gutes, modernes Essen ausgeben, und die offen sind für ein Restaurant, das nur temporär geöffnet ist.
Aufgabenstellung
Unser Logo findet ihr im Dateiupload. Unser Restaurant ist eine alte, aber sehr coole Lagerhalle, die wie ein modernes, gemütliches, lockeres, gehobenes Restaurant eingerichtet ist. Dies sollte auch der Flyer suggerieren! Der Food Truck steht vor dem Restaurant und dient als Küche. Bevorzugt ist das Format DIN-Lang (10,9 x 21,4 Dateiformat, 10,5 x 21,0 Endformat)
Datum: 13.05.17 - 02.07.17
immer von Donnerstags bis Sonntags
Donnerstags: Deluxe Burger & Wine
Freitags bis Sonntags: jedes Wochenende eine neue, kompakte Speisekarte mit modernen Tellergerichten
Uhrzeit: 18.00 - 23.00 Uhr
Küchenzeit: 18.00 - 21.00 Uhr
Internetadresse: www.pelmar.ruhr
facebook: pelmarkuechenwagen

```html
<!DOCTYPE html>
<html lang="de">
<head>
<meta charset="utf-8">
<title>Pop-Up Restaurant – Pelmar Küchenwagen</title>
<link rel="stylesheet" href="https://fonts.googleapis.com/css2?family=Lobster&family=Lora:wght@400;700&display=swap">
<style>
  :root {
    --gold: #f4a71c;
    --gold-shadow: #262626;
    --white: #f4f4f4;
    --ink: #3a3a3a;
    --panel: rgba(38, 38, 38, 0.66);
    --dash: #c8c8c8;
    --hall-light: #9a9a9a;
    --hall-dark: #2b2b2b;
  }
  * { margin: 0; padding: 0; box-sizing: border-box; }
  html, body { width: 1200px; height: 1200px; overflow: hidden; }
  body { font-family: "Lora", serif; }

  .flyer { position: relative; width: 1200px; height: 1200px; overflow: hidden; }

  .hall-photo {
    position: absolute; inset: 0;
    background:
      linear-gradient(200deg, #dadada 0%, #a0a0a0 10%, transparent 24%),
      radial-gradient(ellipse at 98% 50%, #8a8a8a 0%, transparent 28%),
      linear-gradient(180deg, var(--hall-light) 0%, #555 32%, var(--hall-dark) 62%, #363636 100%);
  }

  .panel {
    position: absolute; left: 82px; top: 354px; width: 631px; height: 846px;
    background: var(--panel);
  }
  .panel-edges { position: absolute; left: 0; top: 0; }

  .social {
    position: absolute; left: 56px; top: 90px; transform: translateY(-50%);
    display: flex; align-items: center; gap: 14px;
    color: var(--gold); font-weight: 700; font-size: 28px; line-height: 1;
  }
  .social-mark { width: 28px; height: 28px; background: var(--gold); }

  .web {
    position: absolute; left: 480px; top: 58px; transform: translateY(-50%);
    color: var(--ink); font-weight: 700; font-size: 32px; line-height: 1; letter-spacing: 0.5px;
  }

  .headline { position: absolute; font-family: "Lobster", cursive; color: var(--gold);
    text-shadow: 3px 3px 0 var(--gold-shadow); line-height: 1; white-space: nowrap; }
  .headline-pop { left: 712px; top: 150px; font-size: 132px; transform: rotate(20deg); transform-origin: left center; }
  .headline-restaurant { left: 652px; top: 290px; font-size: 112px; transform: rotate(14deg); transform-origin: left center; }

  .copy { position: absolute; left: 82px; width: 631px; text-align: center; white-space: nowrap;
    line-height: 1; transform: translateY(-50%); }
  .gold { color: var(--gold); }
  .white { color: var(--white); }
  .body-line { font-size: 33px; }
  .script { font-family: "Lobster", cursive; }
  .script-big { font-size: 82px; vertical-align: -6px; }
  .script-mid { font-size: 56px; vertical-align: -3px; }
  .day { font-family: "Lobster", cursive; font-size: 52px; }

  .dates {
    position: absolute; left: 740px; top: 560px; width: 430px; text-align: center;
    color: var(--gold); text-shadow: 2px 2px 0 var(--gold-shadow); line-height: 1.25;
  }
  .dates-range { font-family: "Lobster", cursive; font-size: 50px; line-height: 1.1; }
  .dates-days { font-size: 30px; font-weight: 700; margin-top: 8px; }
  .dates-time { font-size: 30px; margin-top: 14px; color: var(--white); }
  .dates-kitchen { font-size: 26px; color: var(--white); }
</style>
</head>
<body>
<main class="flyer">
  <div class="hall-photo" role="img" aria-label="Schwarzweißfoto einer alten Lagerhalle mit Holzbalken, Ziegelwänden, Leuchter und Kartons"></div>

  <div class="panel"></div>
  <svg class="panel-edges" width="1200" height="1200" aria-hidden="true">
    <line x1="83" y1="354" x2="83" y2="1200" stroke="var(--dash)" stroke-width="7" stroke-dasharray="20 12"/>
    <line x1="712" y1="354" x2="712" y2="1200" stroke="var(--dash)" stroke-width="7" stroke-dasharray="20 12"/>
  </svg>

  <div class="social"><span class="social-mark"></span><span>pelmarkuechenwagen</span></div>
  <div class="web">www.pelmar.ruhr</div>

  <div class="headline headline-pop">Pop-Up</div>
  <div class="headline headline-restaurant">Restaurant</div>

  <section class="dates">
    <p class="dates-range">13.05. – 02.07.17</p>
    <p class="dates-days">immer Donnerstag bis Sonntag</p>
    <p class="dates-time">18.00 – 23.00 Uhr</p>
    <p class="dates-kitchen">Küchenzeit 18.00 – 21.00 Uhr</p>
  </section>

  <p class="copy gold body-line" style="top:453px"><span class="script script-big">Restaurant</span>&nbsp; ist</p>
  <p class="copy gold body-line" style="top:513px">eine alte, aber sehr coole Lagerhalle,</p>
  <p class="copy gold body-line" style="top:577px">die wie ein <span class="script script-big">Restaurant</span></p>
  <p class="copy gold body-line" style="top:639px">eingerichtet ist</p>
  <p class="copy gold body-line" style="top:721px">Der <span class="script script-mid">Food Truck</span> steht vor dem</p>
  <p class="copy gold body-line" style="top:773px">Restaurant und dient als Küche</p>

  <p class="copy white day" style="top:873px">Donnerstags</p>
  <p class="copy white body-line" style="top:929px">Deluxe Burger &amp; Wine</p>
  <p class="copy white day" style="top:1016px">Freitags&nbsp; bis&nbsp; Sonntags</p>
  <p class="copy white body-line" style="top:1069px">jedes WE eine neue, kompakte</p>
  <p class="copy white body-line" style="top:1112px">Speisekarte mit modernen</p>
  <p class="copy white body-line" style="top:1154px">Tellergerichten</p>
</main>
</body>
</html>
```